Psychotherapist need a business card with logo

I am a psychotherapist in need of a business card. The card must have:

Moravia Telvundor
Psicoterapeuta
937 218 604

Psychologists use the greek letter psy, which is the psychologist symbol, but I would prefer something like a mandala, a graphic symbol, an iconic tree, nothing very usual, but something that shows confidence and trust.

Industry/Entity Type

Business

```html
<!DOCTYPE html>
<html lang="es">
<head>
<meta charset="utf-8">
<title>Moravia Telvundor · Psicoterapeuta</title>
<link rel="stylesheet" href="https://fonts.googleapis.com/css2?family=Alex+Brush&family=Didact+Gothic&display=swap">
<style>
  :root {
    --page-bg: #e9e8ec;
    --card-light: #b3b9e6;
    --card-mid: #9aa3dc;
    --card-deep: #8790d2;
    --ink-brown: #56362f;
    --band-brown: #5b3a33;
    --band-light: #c9cdee;
    --ring-white: rgba(255, 255, 255, 0.75);
    --emblem-fill: rgba(255, 255, 255, 0.16);
  }

  * { margin: 0; padding: 0; box-sizing: border-box; }

  html, body {
    width: 1200px;
    height: 900px;
    overflow: hidden;
    background: var(--page-bg);
  }

  .canvas {
    position: relative;
    width: 1200px;
    height: 900px;
    display: flex;
    align-items: center;
    justify-content: center;
  }

  .business-card {
    position: relative;
    width: 840px;
    height: 480px;
    background: linear-gradient(160deg, var(--card-light) 0%, var(--card-mid) 55%, var(--card-deep) 100%);
    box-shadow: 0 18px 40px rgba(40, 30, 60, 0.25);
    overflow: hidden;
  }

  .top-band {
    position: absolute;
    top: 0; left: 0; right: 0;
    height: 30px;
    background:
      linear-gradient(var(--band-brown), var(--band-brown)) 0 0 / 100% 5px no-repeat,
      linear-gradient(var(--band-light), var(--band-light)) 0 5px / 100% 3px no-repeat,
      linear-gradient(var(--band-brown), var(--band-brown)) 0 8px / 100% 16px no-repeat;
  }

  .emblem {
    position: absolute;
    left: 245px;
    top: 92px;
    width: 340px;
    height: 340px;
  }

  .card-text {
    position: absolute;
    left: 0; right: 0;
    top: 170px;
    text-align: center;
    color: var(--ink-brown);
  }

  .holder-name {
    font-family: "Alex Brush", cursive;
    font-weight: 400;
    font-size: 92px;
    line-height: 1;
    margin-left: 10px;
  }

  .holder-role,
  .holder-phone {
    font-family: "Didact Gothic", sans-serif;
    font-size: 32px;
    line-height: 1.35;
    margin-left: -20px;
  }

  .holder-role { margin-top: 6px; }
  .holder-phone { letter-spacing: 2px; }
</style>
</head>
<body>
  <main class="canvas">
    <article class="business-card">
      <div class="top-band"></div>

      <svg class="emblem" viewBox="0 0 340 340" role="img" aria-label="Mandala emblem in soft white lines">
        <circle cx="170" cy="170" r="165" fill="var(--emblem-fill)" stroke="var(--ring-white)" stroke-width="4"/>
      </svg>

      <div class="card-text">
        <h1 class="holder-name">Moravia Telvundor</h1>
        <p class="holder-role">Psicoterapeuta</p>
        <p class="holder-phone">937 218 604</p>
      </div>
    </article>
  </main>
</body>
</html>
```